Kova upkeep RT Sun Systems

Solar power system install
Services and maintenance
wiring, Rewinding and Renovation
Switch Board Upgrade
Power and lighting point
t doesn’t matter how much you spend on quality parts, your solar system will let you down if your design and installation are sub-par. Have your solar system tailored and installed by our Master Electrician and Bright Power Guild Accredited team.

Target Market(s)

sales and installed

Industry/Entity Type

Solar install and retailer

Contact Information for Business Card

Name , Email, Phone Number ,Business address,

Font styles to use
Serif

Colors
0054AA
0677BA
7BADD7
CADEEF
E8F1F8

Requirements
Must have
• clear and bright
Nice to have
• new design
Should not have
• unclear pictures

```html
<!DOCTYPE html>
<html lang="en">
<head>
<meta charset="utf-8">
<title>RT Sun Systems – Business Card</title>
<link rel="stylesheet" href="https://fonts.googleapis.com/css2?family=Cinzel:wght@600&family=Tinos:wght@400;700&display=swap">
<style>
  :root {
    --brand-deep: #0054AA;
    --brand-mid: #0677BA;
    --brand-sky: #7BADD7;
    --brand-pale: #CADEEF;
    --brand-mist: #E8F1F8;
    --accent-yellow: #FFD200;
    --accent-green: #7DC242;
    --sun-orange: #F6A800;
    --white: #FFFFFF;
    --page-bg: #E9EEF3;
  }
  * { box-sizing: border-box; margin: 0; padding: 0; }
  html, body { width: 900px; height: 1200px; overflow: hidden; }
  body {
    background: var(--page-bg);
    font-family: "Tinos", "Times New Roman", serif;
    position: relative;
  }
  .card {
    position: absolute;
    left: 87px;
    width: 733px;
    height: 428px;
    border-radius: 24px;
    overflow: hidden;
    box-shadow: 0 6px 16px rgba(0, 0, 0, 0.25);
  }
  .card-front { top: 125px; background: var(--white); }
  .card-back { top: 641px; background: linear-gradient(135deg, var(--brand-mid) 0%, var(--brand-deep) 60%); }
  .card-shapes { position: absolute; inset: 0; width: 733px; height: 428px; }

  .brand { position: absolute; display: flex; align-items: center; }
  .brand-dot { border-radius: 50%; background: var(--accent-green); flex: none; }
  .brand-name {
    font-family: "Cinzel", "Times New Roman", serif;
    font-weight: 600;
    line-height: 1;
  }
  .brand-name span { display: block; }
  .front-brand { left: 158px; top: 45px; }
  .front-brand .brand-dot { width: 112px; height: 112px; margin-right: 54px; }
  .front-brand .brand-name { color: var(--brand-deep); }
  .front-brand .brand-line-top { font-size: 48px; }
  .front-brand .brand-line-bottom { font-size: 29px; letter-spacing: 0.28em; margin-top: 8px; }

  .contact { position: absolute; color: var(--white); }
  .contact-lines { right: 363px; top: 282px; text-align: right; font-size: 17px; line-height: 27px; }
  .contact-lines .phone { font-weight: 700; font-size: 18px; }
  .contact-lines svg { vertical-align: -2px; margin-left: 8px; }
  .divider { position: absolute; left: 367px; top: 283px; width: 1px; height: 48px; background: rgba(255,255,255,0.7); }
  .person { left: 393px; top: 278px; }
  .person-name { font-family: "Tinos", serif; font-weight: 700; font-size: 30px; letter-spacing: 0.02em; line-height: 34px; }
  .person-role { color: var(--accent-yellow); font-weight: 700; font-size: 17px; letter-spacing: 0.03em; margin-top: 2px; }
  .address { left: 0; right: 0; top: 352px; text-align: center; font-size: 16px; line-height: 23px; }

  .back-brand { left: 40px; top: 36px; }
  .back-brand .brand-dot { width: 78px; height: 78px; margin-right: 12px; }
  .back-brand .brand-name { color: var(--white); }
  .back-brand .brand-line-top { font-size: 37px; }
  .back-brand .brand-line-bottom { font-size: 22px; letter-spacing: 0.3em; margin-top: 4px; }

  .services { position: absolute; left: 42px; top: 139px; list-style: none; color: var(--white); font-size: 17px; }
  .services li { display: flex; align-items: center; height: 33px; }
  .services svg { margin-right: 10px; flex: none; }
  .pitch { position: absolute; left: 42px; top: 316px; width: 440px; color: var(--white); font-size: 13px; line-height: 21.5px; }
</style>
</head>
<body>

  <section class="card card-front">
    <svg class="card-shapes" viewBox="0 0 733 428" aria-hidden="true">
      <defs>
        <linearGradient id="frontBand" x1="0" y1="0" x2="0" y2="1">
          <stop offset="0" stop-color="#0E7FCC"/>
          <stop offset="1" stop-color="#0A63B8"/>
        </linearGradient>
      </defs>
      <path d="M0 272 Q360 190 733 272 L733 428 L0 428 Z" fill="#2A9BDB"/>
      <path d="M0 318 Q330 195 733 282 L733 428 L0 428 Z" fill="var(--accent-yellow)"/>
      <path d="M0 330 Q330 212 733 290 L733 428 L0 428 Z" fill="url(#frontBand)"/>
    </svg>

    <div class="brand front-brand">
      <div class="brand-dot"></div>
      <div class="brand-name"><span class="brand-line-top">RT SUN</span><span class="brand-line-bottom">SYSTEMS</span></div>
    </div>

    <div class="contact contact-lines">
      <div class="phone">555 014 2290
        <svg width="16" height="16" viewBox="0 0 24 24"><path d="M6.6 10.8a15 15 0 0 0 6.6 6.6l2.2-2.2a1 1 0 0 1 1-.25 11.4 11.4 0 0 0 3.6.57 1 1 0 0 1 1 1V20a1 1 0 0 1-1 1A17 17 0 0 1 3 4a1 1 0 0 1 1-1h3.5a1 1 0 0 1 1 1c0 1.25.2 2.45.57 3.6a1 1 0 0 1-.25 1z" fill="var(--accent-yellow)"/></svg>
      </div>
      <div class="email">dana@rtsun.example
        <svg width="16" height="12" viewBox="0 0 16 12"><rect width="16" height="12" fill="var(--accent-yellow)"/><path d="M0 0 L8 7 L16 0" fill="none" stroke="#0A63B8" stroke-width="1.5"/></svg>
      </div>
    </div>
    <div class="divider"></div>
    <div class="contact person">
      <div class="person-name">DANA HALE</div>
      <div class="person-role">CHIEF EXECUTIVE</div>
    </div>
    <div class="contact address">118 Harbor Lane, Suite 20<br>Lakeview, MI 49000</div>
  </section>

  <section class="card card-back">
    <svg class="card-shapes" viewBox="0 0 733 428">
      <defs>
        <linearGradient id="panelScene" x1="0" y1="0" x2="1" y2="1">
          <stop offset="0" stop-color="#1F5FC0"/>
          <stop offset="0.55" stop-color="#5E9BE0"/>
          <stop offset="0.8" stop-color="#BFDDF5"/>
          <stop offset="1" stop-color="#7DBE48"/>
        </linearGradient>
      </defs>
      <path d="M356 0 C296 170 400 372 733 420 L733 0 Z" fill="var(--accent-yellow)"/>
      <path d="M372 0 C314 168 414 360 733 408 L733 0 Z" fill="var(--white)"/>
      <path d="M388 0 C330 165 428 350 733 398 L733 0 Z" fill="url(#panelScene)" role="img" aria-label="Photo of rows of blue solar panels on grass under a bright sky"/>
      <path d="M0 428 L733 428 L733 420 C560 400 470 380 420 352 C470 395 560 420 733 428" fill="none"/>
    </svg>

    <div class="brand back-brand">
      <div class="brand-dot"></div>
      <div class="brand-name"><span class="brand-line-top">RT SUN</span><span class="brand-line-bottom">SYSTEMS</span></div>
    </div>

    <ul class="services">
      <li><svg width="18" height="18" viewBox="0 0 18 18"><circle cx="9" cy="9" r="4" fill="var(--sun-orange)"/><g stroke="var(--sun-orange)" stroke-width="1.6"><line x1="9" y1="0" x2="9" y2="3"/><line x1="9" y1="15" x2="9" y2="18"/><line x1="0" y1="9" x2="3" y2="9"/><line x1="15" y1="9" x2="18" y2="9"/><line x1="2.6" y1="2.6" x2="4.7" y2="4.7"/><line x1="13.3" y1="13.3" x2="15.4" y2="15.4"/><line x1="2.6" y1="15.4" x2="4.7" y2="13.3"/><line x1="13.3" y1="4.7" x2="15.4" y2="2.6"/></g></svg>Solar power system install</li>
      <li><svg width="18" height="18" viewBox="0 0 18 18"><circle cx="9" cy="9" r="4" fill="var(--sun-orange)"/><g stroke="var(--sun-orange)" stroke-width="1.6"><line x1="9" y1="0" x2="9" y2="3"/><line x1="9" y1="15" x2="9" y2="18"/><line x1="0" y1="9" x2="3" y2="9"/><line x1="15" y1="9" x2="18" y2="9"/><line x1="2.6" y1="2.6" x2="4.7" y2="4.7"/><line x1="13.3" y1="13.3" x2="15.4" y2="15.4"/><line x1="2.6" y1="15.4" x2="4.7" y2="13.3"/><line x1="13.3" y1="4.7" x2="15.4" y2="2.6"/></g></svg>Services and maintenance</li>
      <li><svg width="18" height="18" viewBox="0 0 18 18"><circle cx="9" cy="9" r="4" fill="var(--sun-orange)"/><g stroke="var(--sun-orange)" stroke-width="1.6"><line x1="9" y1="0" x2="9" y2="3"/><line x1="9" y1="15" x2="9" y2="18"/><line x1="0" y1="9" x2="3" y2="9"/><line x1="15" y1="9" x2="18" y2="9"/><line x1="2.6" y1="2.6" x2="4.7" y2="4.7"/><line x1="13.3" y1="13.3" x2="15.4" y2="15.4"/><line x1="2.6" y1="15.4" x2="4.7" y2="13.3"/><line x1="13.3" y1="4.7" x2="15.4" y2="2.6"/></g></svg>Wiring, Rewinding and Renovation</li>
      <li><svg width="18" height="18" viewBox="0 0 18 18"><circle cx="9" cy="9" r="4" fill="var(--sun-orange)"/><g stroke="var(--sun-orange)" stroke-width="1.6"><line x1="9" y1="0" x2="9" y2="3"/><line x1="9" y1="15" x2="9" y2="18"/><line x1="0" y1="9" x2="3" y2="9"/><line x1="15" y1="9" x2="18" y2="9"/><line x1="2.6" y1="2.6" x2="4.7" y2="4.7"/><line x1="13.3" y1="13.3" x2="15.4" y2="15.4"/><line x1="2.6" y1="15.4" x2="4.7" y2="13.3"/><line x1="13.3" y1="4.7" x2="15.4" y2="2.6"/></g></svg>Switch Board Upgrade</li>
      <li><svg width="18" height="18" viewBox="0 0 18 18"><circle cx="9" cy="9" r="4" fill="var(--sun-orange)"/><g stroke="var(--sun-orange)" stroke-width="1.6"><line x1="9" y1="0" x2="9" y2="3"/><line x1="9" y1="15" x2="9" y2="18"/><line x1="0" y1="9" x2="3" y2="9"/><line x1="15" y1="9" x2="18" y2="9"/><line x1="2.6" y1="2.6" x2="4.7" y2="4.7"/><line x1="13.3" y1="13.3" x2="15.4" y2="15.4"/><line x1="2.6" y1="15.4" x2="4.7" y2="13.3"/><line x1="13.3" y1="4.7" x2="15.4" y2="2.6"/></g></svg>Power and lighting point</li>
    </ul>

    <p class="pitch">It doesn’t matter how much you spend on quality parts, your solar system will let you down if your design and installation are sub-par. Have your solar system tailored and installed by our Master Electrician and Bright Power Guild Accredited team.</p>
  </section>

</body>
</html>
```